I need a website for my moving company Brisk Haulers LLC. I would like the following text included in my website. I have purchased the domain briskhaulersco.example from nametrellis.example. I am not familiar with SEO or other techniques that help my page on search engines but would like the website to be optimized for Scoutly search engine. I have attached our logo below and would like it to be used in the design. The colors in the logo can be used also in the design.
Home/About Us
At Brisk Haulers LLC, we know moving. It can be difficult, stressful, and a real pain in the backside. But it doesn’t have to be! When you partner with Brisk, you get the benefits of a professional moving team that is licensed and insured for your protection along with years of experience and a dedication to providing the highest quality service, each and every time.
Our Services
We do a wide variety of local moves, including apartments, single-family homes, retirement communities, dorms, condos, and many more! Our movers are trained to protect your belongings and your home – all pieces of furniture are padded and stretch wrapped free of charge, ensuring your items and home are damage-free at the end of your move. Having added stress about packing up your home prior to moving? We’ve got you covered with our full service packing and unpacking services, too.
What You Get
When you partner with BRISK, you’ll get the best service in the industry, as well as:
* The Use of Packing & Moving Materials: The hourly rate includes the use of our dollies, ratchet straps, pads, moving tools, and property protection like floor mats, door-jamb protectors, stairwell protectors, and plenty of muscle!
• Trained, Licensed, and Insured Movers: All of our movers are highly trained to provide you with the best service, and to ensure the protection of you and your items.
• Professional: Honest, Uniformed, Nice, Knowledgeable Service is what you’ll get with every member of our moving teams.
• Custom Service for Every Move: Every move is as unique as the person or business moving. Our training and equipment allows us to customize every project to ensure the very best for every client.
Target Market(s)
Home and Business movers
Industry/Entity Type
Moving Company
Colors
Designer to choose colors to be used in the design.
Requirements
Must have
- 2 sides
Nice to have
- Colorful design with logo included.
Should not have
- animated characters

```html
<!DOCTYPE html>
<html lang="en">
<head>
<meta charset="utf-8">
<title>Brisk Haulers LLC – Ridgeland, MS</title>
<link href="https://fonts.googleapis.com/css2?family=Hind:wght@300;400;500;600;700&family=Open+Sans:wght@400;600;700&display=swap" rel="stylesheet">
<style>
:root{
  --green:#8dc63f;
  --orange:#f7941d;
  --navy:#14283a;
  --ink:#111;
  --text:#6b6b6b;
  --muted:#8a8a8a;
  --line:#e3e3e3;
  --panel:#f3f3f3;
  --white:#fff;
}
*{box-sizing:border-box;margin:0;padding:0}
html,body{width:1200px;height:3854px;overflow:hidden}
body{position:relative;background:var(--white);font-family:"Open Sans",Arial,sans-serif;color:var(--text)}
.abs{position:absolute}
h1,h2,h3,h4{font-family:"Hind",Arial,sans-serif;color:var(--ink);font-weight:500}
.btn{display:inline-flex;align-items:center;justify-content:center;background:var(--orange);color:var(--white);border-radius:30px;font-family:"Hind",Arial,sans-serif;text-transform:uppercase;letter-spacing:.5px;text-decoration:none}

/* top bar */
.topbar{left:0;top:0;width:1200px;height:31px;background:var(--green);color:var(--white);font-size:11px;display:flex;align-items:center;padding:0 85px}
.topbar .info{display:flex;gap:28px;align-items:center}
.topbar .info span{display:flex;gap:6px;align-items:center}
.topbar .social{margin-left:auto;display:flex;gap:18px}
.topbar .social i{display:block;width:11px;height:11px;border-radius:2px;background:rgba(255,255,255,.9)}

/* hero */
.hero{left:0;top:31px;width:1200px;height:594px;background:linear-gradient(100deg,#f4f1ec 0%,#efe9e1 38%,#d8c7b4 62%,#b89a7d 82%,#9a7a5e 100%)}
.brand{left:85px;top:52px;display:flex;align-items:center;gap:10px}
.brand .mark{width:44px;height:44px;background:var(--orange);border-radius:6px}
.brand .name{font-family:"Hind",Arial,sans-serif;font-weight:700;font-size:22px;color:var(--green);letter-spacing:.5px;line-height:1}
.nav{right:85px;top:70px;display:flex;align-items:center;gap:36px;font-family:"Hind",Arial,sans-serif;font-size:14px;color:#222;text-transform:uppercase}
.nav .btn{width:128px;height:38px;font-size:12px}
.hero-title{left:85px;top:240px;line-height:1.1}
.hero-title .l1{display:block;font-weight:300;font-size:56px;letter-spacing:1px;color:#111}
.hero-title .l2{display:block;font-weight:600;font-size:56px;letter-spacing:1px;color:#111}
.hero-book{left:85px;top:403px;width:211px;height:52px;font-size:20px}
.search{left:318px;top:598px;width:564px;height:57px;background:var(--white);border:2px solid #f6c590;border-radius:30px;display:flex;align-items:center;padding:0 30px;font-size:12px;color:#999;box-shadow:0 2px 6px rgba(0,0,0,.05)}
.search svg{margin-left:auto}

/* section headings */
.center{left:0;width:1200px;text-align:center}
.sec-title{font-size:46px;font-weight:500}
.lead{left:285px;width:630px;text-align:center;font-size:16px;line-height:1.65;color:var(--muted)}

/* services */
.svc-title{left:85px;top:1040px;font-size:60px;font-weight:500}
.more{left:985px;top:1056px;width:128px;height:38px;font-size:11px}
.svc{width:330px;display:flex;gap:18px}
.svc .icon{width:58px;flex:none;padding-bottom:10px;border-bottom:2px solid var(--orange);display:flex;justify-content:center}
.svc .icon i{display:block;width:58px;height:58px;border-radius:4px}
.svc h4{font-size:18px;font-weight:400;margin-bottom:4px}
.svc p{font-size:11px;line-height:1.45;color:#555}

/* experienced */
.exp-photo{left:85px;top:1496px;width:514px;height:401px;background:linear-gradient(135deg,#9c8d78 0%,#c9c2b6 40%,#7d8da3 70%,#5e6e86 100%)}
.exp-box{left:599px;top:1496px;width:514px;height:401px;border:1px solid #f6d1a6;border-left:none;text-align:center;padding:56px 50px 0}
.exp-box h3{font-size:36px;font-weight:500}
.exp-box .rule{width:90px;height:2px;background:var(--orange);margin:12px auto 18px}
.exp-box p{font-size:13px;line-height:1.7;color:var(--muted)}
.exp-box .btn{width:128px;height:38px;font-size:11px;margin-top:22px}

/* guarantee */
.guar{left:0;top:1992px;width:1200px;height:270px;background:var(--green);text-align:center;color:var(--white)}
.guar h2{color:var(--white);font-size:40px;font-weight:500;margin-top:44px}
.guar p{width:630px;margin:18px auto 0;font-size:16px;line-height:1.65}
.guar-row{left:0;top:2262px;width:1200px;height:156px;display:flex}
.guar-row div{display:flex;flex-direction:column;align-items:center;justify-content:center;color:var(--white);font-size:17px;line-height:1.3;text-align:center}
.g-a{width:460px;background:var(--orange)}
.g-b{width:273px;background:var(--green)}
.g-c{width:467px;background:var(--orange)}

/* appointment */
.appt{left:170px;top:2544px;width:321px;height:360px;background:var(--panel);border-radius:0 0 40px 0;text-align:center;padding-top:42px}
.appt h4{font-size:21px;font-weight:500;color:#222}
.appt .field{width:230px;margin:0 auto;padding:16px 0 10px;border-bottom:1px solid var(--line);font-size:12px;color:#999}
.appt .field:first-of-type{margin-top:22px}
.appt .btn{width:210px;height:52px;font-size:18px;margin-top:30px;box-shadow:0 4px 6px rgba(0,0,0,.15)}
.mv{left:570px;top:2594px;width:470px}
.mv h3{font-size:42px;font-weight:600}
.mv p{font-size:13px;line-height:1.7;color:var(--muted);margin-top:18px}
.mv .price{font-family:"Hind",Arial,sans-serif;font-size:32px;color:var(--green);font-weight:500;margin-top:20px}
.mv .price .sep{color:#bbb}
.mv .price b{font-weight:600}

/* map */
.map{left:0;top:3218px;width:1200px;height:169px;background:linear-gradient(180deg,#eceae6,#e4e2dd)}
.map-label{left:0;top:3290px;width:1200px;text-align:center;font-family:"Hind",Arial,sans-serif;font-weight:700;font-size:22px;color:var(--green)}
.map-label .pin{display:block;margin:0 auto 2px}
.map-label .rule{width:60px;height:2px;background:var(--orange);margin:4px auto 0}

/* footer info */
.finfo{top:3444px}
.finfo h4{font-size:21px;font-weight:600;color:#222;margin-bottom:12px}
.finfo p{font-size:13px;line-height:1.55;color:var(--muted)}
.vr{top:3455px;width:3px;height:110px;background:#f6c590}
.send{width:156px;height:40px;font-size:11px;margin-top:18px}

/* footer */
.footer{left:0;top:3605px;width:1200px;height:249px;background:var(--navy);text-align:center;color:var(--white)}
.flinks{display:flex;justify-content:center;gap:20px;margin-top:112px;font-size:13px}
.fsocial{display:flex;justify-content:center;gap:26px;margin-top:22px}
.fsocial i{display:block;width:26px;height:26px;border:1px solid rgba(255,255,255,.8);border-radius:50%}
.copy{font-size:10px;margin-top:20px;color:rgba(255,255,255,.85)}
</style>
</head>
<body>

<div class="abs topbar">
  <div class="info">
    <span><svg width="10" height="10" viewBox="0 0 24 24" fill="#fff"><path d="M6.6 10.8a15.1 15.1 0 0 0 6.6 6.6l2.2-2.2a1 1 0 0 1 1-.25 11.4 11.4 0 0 0 3.6.57 1 1 0 0 1 1 1V20a1 1 0 0 1-1 1A17 17 0 0 1 3 4a1 1 0 0 1 1-1h3.5a1 1 0 0 1 1 1c0 1.25.2 2.45.57 3.6a1 1 0 0 1-.25 1z"/></svg>(601) 555-0148</span>
    <span><svg width="10" height="12" viewBox="0 0 24 24" fill="#fff"><path d="M12 2a7 7 0 0 0-7 7c0 5.2 7 13 7 13s7-7.8 7-13a7 7 0 0 0-7-7zm0 9.5A2.5 2.5 0 1 1 12 6.5a2.5 2.5 0 0 1 0 5z"/></svg>412 Alder Row, Ridgeland, MS 39157, US</span>
  </div>
  <div class="social"><i></i><i></i><i></i><i></i><i></i></div>
</div>

<div class="abs hero" role="img" aria-label="Photo of a smiling woman leaning on a moving box in a bright room"></div>

<div class="abs brand"><span class="mark"></span><span class="name">BRISK HAULERS</span></div>

<nav class="abs nav">
  <span>Home</span><span>About Us</span><span>Our Services</span><span>Contact</span>
  <a class="btn" href="#">Book Today</a>
</nav>

<h1 class="abs hero-title"><span class="l1">BRISK HAULERS LLC</span><span class="l2">RIDGELAND, MS</span></h1>
<a class="abs btn hero-book" href="#">Book Now</a>

<div class="abs search">Search here
  <svg width="20" height="20" viewBox="0 0 24 24" fill="none" stroke="#555" stroke-width="2"><circle cx="10" cy="10" r="7"/><path d="M15 15l6 6"/></svg>
</div>

<h2 class="abs center sec-title" style="top:718px">About Us</h2>
<p class="abs lead" style="top:794px">This is Pixelwright's version &nbsp;of Lorem Ipsum. Proin gravida nibh vel velit auctor aliquet. Aenean sollicitudin, lorem quis bibendum auctor, nisi elit consequat ipsum, nec sagittis sem nibh id elit. Duis sed odio sit amet nibh vulputate.</p>
<a class="abs btn" href="#" style="left:495px;top:912px;width:210px;height:50px;font-size:16px">Read More</a>

<h2 class="abs svc-title">Our Services</h2>
<a class="abs btn more" href="#">Many More</a>

<div class="abs svc" style="left:85px;top:1168px"><div class="icon"><i role="img" aria-label="Apartment icon" style="background:#f26b3a"></i></div><div><h4>Including Apartments</h4><p>This is Pixelwright's version Lorem Ipsum. Proin gravida nibh vel velit auctor aliquet. Aenean sollicitudin, lorem quis bibendum</p></div></div>
<div class="abs svc" style="left:437px;top:1168px"><div class="icon"><i role="img" aria-label="House icon" style="background:#8dc63f"></i></div><div><h4>Single-Family Homes</h4><p>This is Pixelwright's version Lorem Ipsum. Proin gravida nibh vel velit auctor aliquet. Aenean sollicitudin, lorem quis bibendum</p></div></div>
<div class="abs svc" style="left:797px;top:1168px"><div class="icon"><i role="img" aria-label="Retirement community icon" style="background:#d9dde2"></i></div><div><h4>Retirement Communities</h4><p>This is Pixelwright's version Lorem Ipsum. Proin gravida nibh vel velit auctor aliquet. Aenean sollicitudin, lorem quis bibendum</p></div></div>
<div class="abs svc" style="left:85px;top:1298px"><div class="icon"><i role="img" aria-label="Dorm icon" style="background:#f2b24a"></i></div><div><h4>Dorms</h4><p>This is Pixelwright's version Lorem Ipsum. Proin gravida nibh vel velit auctor aliquet. Aenean sollicitudin, lorem quis bibendum</p></div></div>
<div class="abs svc" style="left:437px;top:1298px"><div class="icon"><i role="img" aria-label="Condo icon" style="background:#dfe3e6"></i></div><div><h4>Condos</h4><p>This is Pixelwright's version Lorem Ipsum. Proin gravida nibh vel velit auctor aliquet. Aenean sollicitudin, lorem quis bibendum</p></div></div>
<div class="abs svc" style="left:797px;top:1298px"><div class="icon"><i role="img" aria-label="Local move icon" style="background:#cfd6df"></i></div><div><h4>Local Moves</h4><p>This is Pixelwright's version Lorem Ipsum. Proin gravida nibh vel velit auctor aliquet. Aenean sollicitudin, lorem quis bibendum</p></div></div>

<div class="abs exp-photo" role="img" aria-label="Photo of two movers in blue uniforms carrying a white sofa out of a truck"></div>
<div class="abs exp-box">
  <h3>Experienced &amp; Reliable</h3>
  <div class="rule"></div>
  <p>At Brisk Haulers LLC, we know moving. It can be difficult, stressful, and a real pain in the backside. But it doesn't have to be! When you partner with Brisk, you get the benefits of a professional moving team that is licensed and insured for your protection along with years of experience and a dedication to providing the highest quality service, each and every time.</p>
  <a class="btn" href="#">Read More</a>
</div>

<section class="abs guar">
  <h2>Our Gaurantee</h2>
  <p>This is Pixelwright's version &nbsp;of Lorem Ipsum. Proin gravida nibh vel velit auctor aliquet. Aenean sollicitudin, lorem quis bibendum auctor, nisi elit consequat ipsum, nec sagittis sem nibh id elit. Duis sed odio sit amet nibh vulputate.</p>
</section>
<div class="abs guar-row">
  <div class="g-a">The unlimited use of packing &amp;<br>moving materials</div>
  <div class="g-b"><svg width="40" height="30" viewBox="0 0 40 30" fill="none" stroke="#fff" stroke-width="2" style="margin-bottom:18px"><path d="M3 5l11-3 12 3 11-3v23l-11 3-12-3-11 3z"/><path d="M14 2v23M26 5v23"/></svg>Trained, Licensed, and<br>Insured Movers</div>
  <div class="g-c">A Professional service catering<br>to your specific needs</div>
</div>

<div class="abs appt">
  <h4>Book an Appointment</h4>
  <div class="field">Your name</div>
  <div class="field">Please enter your e-mail or phone</div>
  <div class="field">Your question</div>
  <a class="btn" href="#">Book Now</a>
</div>

<div class="abs mv">
  <h3>Moving Service</h3>
  <p>At Brisk Haulers LLC, we know moving. It can be difficult, stressful, and a real pain in the backside. But it doesn't have to be! When you partner with Brisk, you get the benefits of a professional moving team that is licensed and insured for your protection along with years of experience and a dedication to providing the highest quality service, each and every time.</p>
  <div class="price">1 hour<span class="sep"> | </span><b>$125.00</b></div>
</div>

<h2 class="abs center sec-title" style="top:3004px">Contact Us</h2>
<p class="abs lead" style="top:3080px">This is Pixelwright's version &nbsp;of Lorem Ipsum. Proin gravida nibh vel velit auctor aliquet. Aenean sollicitudin, lorem quis bibendum auctor, nisi elit consequat ipsum, nec sagittis sem nibh id elit. Duis sed odio sit amet nibh vulputate.</p>

<div class="abs map" role="img" aria-label="Street map of the Ridgeland area"></div>
<div class="abs map-label">
  <svg class="pin" width="18" height="22" viewBox="0 0 24 30" fill="#f7941d"><path d="M12 0a10 10 0 0 0-10 10c0 7.5 10 20 10 20s10-12.5 10-20A10 10 0 0 0 12 0zm0 14a4 4 0 1 1 0-8 4 4 0 0 1 0 8z"/></svg>
  OPEN MAP
  <div class="rule"></div>
</div>

<div class="abs finfo" style="left:85px;width:380px">
  <h4>Schedule Your Move</h4>
  <p>To arrange movers, please contact us at your convenience. &nbsp;We look forward to meeting you soon.</p>
</div>
<div class="abs vr" style="left:515px"></div>
<div class="abs finfo" style="left:575px;width:300px">
  <h4>Brisk Haulers LLC</h4>
  <p>412 Alder Row, Ridgeland, MS 39157, US<br>(601) 555-0148</p>
</div>
<div class="abs vr" style="left:903px"></div>
<div class="abs finfo" style="left:956px;width:200px">
  <h4>Service Area</h4>
  <p>Central Mississippi</p>
  <a class="btn send" href="#">Send Message</a>
</div>

<footer class="abs footer">
  <div class="flinks"><span>Home</span><span>About</span><span>Services</span><span>Blog</span><span>Contact</span></div>
  <div class="fsocial"><i></i><i></i><i></i></div>
  <div class="copy">Copyright © 2017 Brisk Haulers LLC - All Rights Reserved.</div>
</footer>

</body>
</html>
```